Accommodation business card design

We need a business card designed for our long-term accommodation business based in Australia. The business card must match the style of the attached letterhead and logo. The same contact details that are on the letterhead will also go on the card except that the card must list the contact details in the following order:phone, email, home address, ABN.

The card will be printed on .76mm white pvc plastic (same as credit cards), printed both sides and will be silver foil stamped on at least one side (preferably 2 sides) The design template is attached, but please go to www.qz-cardworks.com.au for more specs.

The only other addition the card will be my name: Dalwyn Prothero

Industry/Entity Type

Accommodation

```html
<!DOCTYPE html>
<html lang="en">
<head>
<meta charset="utf-8">
<title>Highridge Accommodation – Business Card</title>
<link href="https://fonts.googleapis.com/css2?family=Ubuntu:wght@400;500;700&display=swap" rel="stylesheet">
<style>
  :root {
    --backdrop: #3a2c24;
    --card-light: #d9cfc1;
    --card-mid: #c7b9a6;
    --maroon: #8a2a50;
    --brown: #9b5a50;
    --ink: #6e2743;
    --text-soft: #5c4a48;
    --white: #ffffff;
  }
  * { box-sizing: border-box; margin: 0; padding: 0; }
  html, body {
    width: 1200px; height: 549px; overflow: hidden;
    background: var(--backdrop);
    font-family: "Ubuntu", Arial, sans-serif;
  }
  .canvas { position: relative; width: 1200px; height: 549px; }
  .card {
    position: absolute; width: 453px; height: 283px;
    border-radius: 18px; overflow: hidden;
    background: linear-gradient(160deg, var(--card-light), var(--card-mid));
    box-shadow: 0 6px 18px rgba(0,0,0,.35);
  }
  .card--front { left: 105px; top: 112px; }
  .card--back  { left: 585px; top: 108px; height: 282px; }

  .brand { position: absolute; display: flex; align-items: center; gap: 10px; }
  .brand__square { width: 54px; height: 54px; background: var(--maroon); border-radius: 4px; }
  .brand__name {
    color: var(--maroon); font-weight: 700; line-height: 1;
    text-transform: uppercase;
  }
  .brand__name span { display: block; }
  .brand__name .brand__line1 { font-size: 27px; letter-spacing: .5px; }
  .brand__name .brand__line2 { font-size: 14.5px; margin-top: 3px; }
  .card--front .brand { left: 30px; top: 76px; }
  .card--back .brand { left: 138px; top: 148px; }
  .card--back .brand__square { width: 46px; height: 46px; }
  .card--back .brand__line1 { font-size: 23px; }
  .card--back .brand__line2 { font-size: 12.5px; }

  .divider {
    position: absolute; left: 247px; top: 45px; width: 1px; height: 128px;
    background: var(--text-soft); opacity: .6;
  }
  .contacts {
    position: absolute; left: 260px; top: 48px;
    list-style: none; font-size: 10.5px; color: var(--ink); line-height: 1.4;
  }
  .contacts li { display: flex; gap: 6px; margin-bottom: 7px; }
  .contacts svg { flex: none; margin-top: 1px; }
  .abn { position: absolute; left: 268px; top: 162px; font-size: 10.5px; color: var(--text-soft); }

  .band { position: absolute; left: 0; top: 0; }
  .holder {
    position: absolute; left: 26px; top: 246px;
    color: var(--white); font-size: 17px; font-weight: 400;
  }
</style>
</head>
<body>
<main class="canvas">
  <section class="card card--front" aria-label="Card front">
    <svg class="band" width="453" height="283" viewBox="0 0 453 283" aria-hidden="true">
      <path d="M140 205 C260 218 370 206 453 176 L453 198 C350 230 240 226 140 205 Z" fill="var(--maroon)"/>
      <path d="M0 222 C150 240 300 236 453 196 L453 283 L0 283 Z" fill="var(--brown)"/>
    </svg>

    <div class="brand">
      <div class="brand__square"></div>
      <p class="brand__name"><span class="brand__line1">Highridge</span><span class="brand__line2">Accommodation</span></p>
    </div>

    <div class="divider"></div>

    <ul class="contacts">
      <li>
        <svg width="10" height="10" viewBox="0 0 10 10"><circle cx="5" cy="5" r="5" fill="var(--maroon)"/><path d="M5 2 L8 5 H7 V8 H3 V5 H2 Z" fill="#fff"/></svg>
        <span>PO Box 7318,<br>Carrow Mail Centre,<br>QLD 4790</span>
      </li>
      <li>
        <svg width="10" height="10" viewBox="0 0 10 10"><circle cx="5" cy="5" r="5" fill="var(--maroon)"/><path d="M3.2 2.5 L4.3 3.6 L3.8 4.3 C4.2 5.1 4.9 5.8 5.7 6.2 L6.4 5.7 L7.5 6.8 L6.8 7.6 C4.9 7.3 2.7 5.1 2.4 3.2 Z" fill="#fff"/></svg>
        <span>0400 555 218</span>
      </li>
      <li>
        <svg width="10" height="10" viewBox="0 0 10 10"><circle cx="5" cy="5" r="5" fill="var(--maroon)"/><rect x="2.3" y="3.2" width="5.4" height="3.6" fill="#fff"/><path d="M2.3 3.2 L5 5.2 L7.7 3.2" stroke="var(--maroon)" stroke-width=".6" fill="none"/></svg>
        <span>dalwyn.prothero@mailbox.net.au</span>
      </li>
    </ul>

    <p class="abn">ABN 51 804 227 169</p>

    <p class="holder">Dalwyn Prothero</p>
  </section>

  <section class="card card--back" aria-label="Card back">
    <div class="brand">
      <div class="brand__square"></div>
      <p class="brand__name"><span class="brand__line1">Highridge</span><span class="brand__line2">Accommodation</span></p>
    </div>
  </section>
</main>
</body>
</html>
```